Dance school needs a poster to promote our annual concert

I have a dance school called 'The Marcella Dunwoody Dancers'
See designs from previous years
This year's concert theme is Brant Holloway animation movies
The title of the concert is "glimmeRa"
Dance items will be choreographed to; “Quiet Orchard”, Copper Heron”, “The Nine Lanterns”, “The Fox Regent”, “Temrik”, “Willow & the Warden” & “Pipsqueeve”.
I need a colorful A4 (portrait) poster promoting the concert.

Target Market(s)

Families of students & dance community

Industry/Entity Type

Dance Studio

Font styles to use
Other font styles liked:
• "Mistral" for my my name (see examples supplied)

Colors

Designer to choose colors to be used in the design.

Requirements
Must have
• Must Have:
• - The poster must include the following information:
• 'The Marcella Dunwoody Dancers'
• presents
• "glimmeRa"
• (Font for my name is "Mistral")
• Saturday 18th November 2017
• Corbett Hall,
• Halverd Grammar Elmstead.

```html
<!DOCTYPE html>
<html lang="en">
<head>
<meta charset="utf-8">
<title>glimmeRa – The Marcella Dunwoody Dancers</title>
<link rel="stylesheet" href="https://fonts.googleapis.com/css2?family=Cinzel:wght@400;600&family=Cormorant+Garamond:wght@500&family=Dancing+Script:wght@600&display=swap">
<style>
  :root {
    --backdrop: #e4e4e2;
    --poster-black: #000000;
    --ink-white: #ffffff;
    --accent-red: #d8141c;
    --hair-brown: #3a2416;
    --skin-warm: #b88a6e;
    --rose-red: #c0151b;
    --rose-deep: #5e0508;
  }
  * { margin: 0; padding: 0; box-sizing: border-box; }
  html, body {
    width: 1200px; height: 1000px; overflow: hidden;
    background: var(--backdrop);
  }
  .poster {
    position: absolute;
    left: 325px; top: 30px;
    width: 550px; height: 940px;
    background: var(--poster-black);
    color: var(--ink-white);
    overflow: hidden;
  }
  .hero-art {
    position: absolute;
    left: 80px; top: 20px;
    width: 420px; height: 680px;
    background:
      radial-gradient(ellipse 46% 28% at 50% 74%, var(--rose-red) 0%, #9e0f14 45%, var(--rose-deep) 75%, rgba(0,0,0,0) 100%),
      radial-gradient(ellipse 22% 10% at 50% 36%, var(--skin-warm) 0%, rgba(184,138,110,0.4) 60%, rgba(0,0,0,0) 100%),
      radial-gradient(ellipse 42% 45% at 50% 38%, var(--hair-brown) 0%, #1d120b 55%, rgba(0,0,0,0) 100%);
  }
  .school-mark {
    position: absolute; top: 58px; left: 0; width: 100%;
    display: flex; justify-content: center; align-items: center; gap: 8px;
    font-family: "Cinzel", serif; font-weight: 600; font-size: 20px; letter-spacing: 2px;
  }
  .school-mark .dot {
    width: 10px; height: 10px; border-radius: 50%; background: var(--ink-white);
  }
  .school-name {
    position: absolute; top: 132px; left: 0; width: 100%;
    text-align: center;
    font-family: "Dancing Script", cursive; font-weight: 600; font-size: 34px;
  }
  .presents {
    position: absolute; top: 190px; left: 0; width: 100%;
    text-align: center;
    font-family: "Cinzel", serif; font-size: 15px; letter-spacing: 5px;
  }
  .concert-title {
    position: absolute; top: 648px; left: 0; width: 100%;
    text-align: center;
    font-family: "Cormorant Garamond", serif; font-weight: 500; font-size: 96px;
    line-height: 1; letter-spacing: 1px;
  }
  .concert-title .accent { color: var(--accent-red); }
  .concert-date {
    position: absolute; top: 770px; left: 0; width: 100%;
    text-align: center;
    font-family: "Cinzel", serif; font-weight: 600; font-size: 22px; letter-spacing: 1px;
  }
  .divider {
    position: absolute; top: 808px; left: 160px; width: 230px; height: 8px;
  }
  .venue {
    position: absolute; top: 852px; left: 0; width: 100%;
    text-align: center;
    font-family: "Cinzel", serif; font-size: 17px; line-height: 30px;
  }
</style>
</head>
<body>
  <main class="poster">
    <div class="hero-art" role="img" aria-label="Photo of a woman with long dark hair, eyes covered by hands from behind, holding a large red rose"></div>

    <div class="school-mark"><span class="dot"></span><span>MDD</span></div>
    <div class="school-name">The Marcella Dunwoody Dancers</div>
    <div class="presents">PRESENTS</div>

    <h1 class="concert-title">glimme<span class="accent">R</span>a</h1>
    <div class="concert-date">SATURDAY 18TH NOVEMBER 2017</div>

    <svg class="divider" viewBox="0 0 230 8" aria-hidden="true">
      <line x1="0" y1="4" x2="230" y2="4" stroke="#ffffff" stroke-width="1.2"/>
    </svg>

    <div class="venue">
      Corbett Hall,<br>
      Halverd Grammar Elmstead
    </div>
  </main>
</body>
</html>
```